Promo flyer

Simple, clean flyer to hand to customers during a wedding expo. These will be handed out to foot traffic.
Flyer must be easy to read, simple but pretty and in line with our branding.
Logo must be shown
Images and or styling tools
Please look at our website to get a feel for the brand/colours/etc.
www.larkmeretress.co.uk
The images attached are samples from the website....something along these lines. Images can be used alone and wording separate.
HD images of the girls alone can be provided so its best quality for print.

Mention
-Shop our luxurious hair extensions & styling tools
-www.larkmeretress.co.uk
-QJ50 = 50% off all styling tools
-Complimentary colour match for hair extensions. Email uk@larkmeretress.com.

Industry/Entity Type

Wedding

Requirements
Must have
• Logo must be shown
• Images and or styling tools
• BEFORE & AFTER Images (1 before and after) - refer to this link below.
• https://www.larkmeretress.com/pages/before-afters-see-the-difference
• Please look at our website to get a feel for the brand/colours/etc.
• www.larkmeretress.co.uk
• The images attached are samples from the website....something along these lines. Images can be used alone and wording separate.
Nice to have
• Water colour behind the discount codes so this stands out

```html
<!DOCTYPE html>
<html lang="en">
<head>
<meta charset="utf-8">
<title>Larkmere Tress – Promo Flyer</title>
<link rel="stylesheet" href="https://fonts.googleapis.com/css2?family=Philosopher:wght@400;700&family=Mulish:wght@300;400;700&display=swap">
<style>
  :root {
    --brand-pink: #e0457f;
    --brand-pink-soft: #f2a9c4;
    --ink: #1c1c1c;
    --paper: #ffffff;
    --silver: #d9d9dc;
    --stage: #ececec;
    --photo-dark: #3a2e2b;
    --photo-light: #d8cdc4;
  }
  * { margin: 0; padding: 0; box-sizing: border-box; }
  html, body { width: 1027px; height: 1200px; overflow: hidden; background: var(--stage); }
  .flyer {
    position: absolute; left: 165px; top: 105px;
    width: 697px; height: 985px;
    background: var(--paper); overflow: hidden;
    font-family: "Mulish", "Helvetica Neue", sans-serif;
  }
  .brand { position: absolute; left: 60px; top: 58px; width: 200px; text-align: center; }
  .brand-ring {
    width: 128px; height: 128px; margin: 0 auto;
    border: 2px solid var(--brand-pink); border-radius: 50%;
  }
  .brand-name {
    margin-top: 17px; color: var(--brand-pink);
    font-size: 14px; letter-spacing: 3px; font-weight: 400;
  }
  .headline {
    position: absolute; left: 75px; top: 270px;
    font-family: "Philosopher", Georgia, sans-serif;
    font-size: 44px; line-height: 48px; color: var(--brand-pink); font-weight: 400;
  }
  .headline .lead { color: var(--ink); display: block; }
  .hero-photo {
    position: absolute; left: 338px; top: 28px; width: 334px; height: 520px;
    background: linear-gradient(180deg, var(--photo-dark) 0%, #4a3b36 55%, var(--photo-light) 100%);
  }
  .wave { position: absolute; left: 0; top: 420px; width: 697px; height: 565px; }
  .offer-title {
    position: absolute; left: 52px; top: 598px;
    color: var(--paper); font-size: 21px; line-height: 36px; font-weight: 300; letter-spacing: 0.2px;
  }
  .tools { position: absolute; left: 51px; top: 688px; display: flex; gap: 9px; }
  .tool {
    width: 108px; height: 108px; border-radius: 50%;
    border: 3px solid var(--brand-pink-soft);
    background: linear-gradient(135deg, #f4f4f4, #d6d6d6);
  }
  .promo-code {
    position: absolute; left: 50px; top: 832px; width: 361px; height: 37px;
    background: var(--paper); border-radius: 18px;
    border: 2px solid var(--brand-pink-soft);
    font-family: "Philosopher", Georgia, sans-serif; font-size: 22px; font-weight: 700;
    color: var(--brand-pink); line-height: 33px; padding-left: 9px; white-space: nowrap;
  }
  .colour-match {
    position: absolute; left: 52px; top: 891px;
    font-size: 14px; line-height: 20px; color: var(--ink);
  }
  .website {
    position: absolute; right: 45px; top: 929px;
    font-size: 15px; font-weight: 700; color: var(--ink);
  }
  .compare { position: absolute; left: 487px; width: 151px; height: 140px; background: var(--paper); }
  .compare.before { top: 585px; }
  .compare.after { top: 743px; }
  .compare-shot {
    position: absolute; inset: 0;
    background: linear-gradient(180deg, #5a4a45 0%, var(--photo-dark) 60%, #cdbfb5 100%);
  }
  .compare-tag {
    position: absolute; top: 22px; width: 42px; height: 10px;
    background: var(--brand-pink-soft); color: var(--paper);
    font-size: 5px; letter-spacing: 1px; line-height: 10px; text-align: center;
  }
  .before .compare-tag { left: 0; }
  .after .compare-tag { right: 0; top: 24px; }
</style>
</head>
<body>
  <main class="flyer">
    <div class="brand">
      <div class="brand-ring"></div>
      <p class="brand-name">LARKMERE TRESS</p>
    </div>

    <h1 class="headline"><span class="lead">Instantly</span>Get Longer<br>Thicker Hair</h1>

    <div class="hero-photo" role="img" aria-label="Photo of a model with long, voluminous dark wavy hair extensions"></div>

    <svg class="wave" viewBox="0 0 697 565" aria-hidden="true">
      <path d="M0 0 C180 95 420 130 697 10 L697 565 L0 565 Z" fill="var(--silver)"/>
      <path d="M0 14 C180 108 420 140 697 38 L697 565 L0 565 Z" fill="var(--paper)"/>
      <path d="M0 26 C180 118 420 146 697 60 L697 565 L0 565 Z" fill="var(--brand-pink)"/>
    </svg>

    <p class="offer-title">SHOP OUR LUXURIOUS HAIR<br>EXTENSIONS &amp; STYLING TOOLS</p>

    <div class="tools">
      <div class="tool" role="img" aria-label="Photo of an interchangeable curling wand set"></div>
      <div class="tool" role="img" aria-label="Photo of a slim hair straightener"></div>
      <div class="tool" role="img" aria-label="Photo of a wide-plate hair straightener"></div>
    </div>

    <p class="promo-code">QJ50 = 50% off all styling tools</p>

    <p class="colour-match">Complimentary colour match<br>for hair extensions.<br>Email uk@larkmeretress.com</p>

    <p class="website">www.larkmeretress.co.uk</p>

    <div class="compare before">
      <div class="compare-shot" role="img" aria-label="Photo of hair from behind before extensions"></div>
      <span class="compare-tag">BEFORE</span>
    </div>
    <div class="compare after">
      <div class="compare-shot" role="img" aria-label="Photo of longer, fuller hair from behind after extensions"></div>
      <span class="compare-tag">AFTER</span>
    </div>
  </main>
</body>
</html>
```